Velvet Ladder Flyer, eyecatching

Hi,
To give you an idea of the business for design purposes, #VelvettLadder is predominantly a recruitment and people development business, ran by me dedicated to training & assisting others in achieving extra income (pt or f/t) around their current commitments, people also have the opportunity to build their own business brand with my support. My brand colours are Red, White and Black, and I would like to incorporate the following text;

#VelvetLadder

Recruiting now! Start today & start earning!

Would you like an extra income, for…
A holiday?…A new car?…Lifestyle changes?
(Can you put a tick box or something similar adjacent to each)

Are you facing…
Redundancy? Birth of a new child? Hefty bills?

If so, I have the solution.

Contact Rosalind Pettigrew today: (can you insert the appropriate icon for each of the contact details)
Tel: 07945 618274
Twitter: @Velvet_Ladder
Email: Rosalind@velvetladder.co.uk
Facebook: www.pagehub.net/rosandvelvetladder

Target Market(s)

Women aged 25-45 years, possibly busy mums too, wanting to earn additinal income to allow them more choices, be it family time, money, new challenge, meeting new people, personal development

Industry/Entity Type

Health And Wellness

Font styles to use
Serif
Sans Serif
Decorative
Script

Colors
ec1f27
ffffff
000000

Requirements
Must have
• My heels logo, be clear concise and eye catching, I also have the following strap line if you wish to use;
• Empowering other to achieve
• Also I have attached a closeup picture of myself but would ideally only like half my face to appear (leftside) similar to the other picture posted - if you can
Nice to have
• Perhaps adding other forms of graphics, or the 3rd picture I have attached with myself...possibly just the shoes though
Should not have
• Too many colours

```html
<!DOCTYPE html>
<html lang="en">
<head>
<meta charset="utf-8">
<title>Velvet Ladder Flyer</title>
<link href="https://fonts.googleapis.com/css2?family=Abril+Fatface&family=Open+Sans:wght@600;700;800&family=Roboto+Slab:wght@700;800&display=swap" rel="stylesheet">
<style>
  :root {
    --red: #c8101a;
    --black: #131213;
    --white: #ffffff;
    --stage: #ececec;
    --icon-fill: #d9d9d9;
    --social: #4a8fd0;
    --social-dark: #3b5998;
  }
  * { margin: 0; padding: 0; box-sizing: border-box; }
  html, body { width: 1200px; height: 1170px; overflow: hidden; background: var(--stage); }
  .flyer {
    position: absolute; left: 202px; top: 20px;
    width: 826px; height: 1172px;
    background: var(--white);
    transform: scale(0.964); transform-origin: top left;
    overflow: hidden;
    font-family: "Open Sans", sans-serif;
  }
  .dark-field { position: absolute; inset: 0; }
  .photo { position: absolute; top: 17px; height: 376px; width: 182px; }
  .photo-left { left: 17px; background: linear-gradient(160deg, #d7d9db 0%, #9a9c9e 35%, #2a2a2c 70%, #111 100%); }
  .photo-right { left: 211px; background: linear-gradient(200deg, #e9e9ef 0%, #d8c1b6 45%, #b98e80 75%, #3a2a2a 100%); }
  .logo-disc {
    position: absolute; left: 64px; top: 65px; width: 270px; height: 270px;
    border-radius: 50%; background: var(--white);
    display: flex; align-items: center; justify-content: center; text-align: center;
    font-family: "Roboto Slab", serif; font-weight: 700; font-size: 30px; line-height: 1.15; color: var(--black);
  }
  .brand { position: absolute; left: 423px; top: 152px; width: 380px; text-align: center; }
  .brand-name { font-family: "Roboto Slab", serif; font-weight: 800; font-size: 41px; color: var(--black); letter-spacing: -0.5px; white-space: nowrap; }
  .brand-tagline { font-weight: 700; font-size: 19px; color: var(--red); margin-top: 2px; white-space: nowrap; }
  .headline {
    position: absolute; left: 0; width: 826px; top: 480px; text-align: center;
    font-family: "Abril Fatface", serif; font-size: 70px; color: var(--red); letter-spacing: -1px; line-height: 1;
  }
  .subhead {
    position: absolute; left: 0; width: 826px; top: 552px; text-align: center;
    font-family: "Roboto Slab", serif; font-weight: 700; font-size: 37px; color: var(--white); line-height: 1;
  }
  .col-heading { position: absolute; font-weight: 700; font-size: 19px; line-height: 1.15; color: var(--white); }
  .col-heading.left { left: 133px; top: 637px; }
  .col-heading.right { left: 470px; top: 650px; }
  .divider { position: absolute; left: 397px; top: 640px; width: 2px; height: 230px; background: var(--red); }
  .pill {
    position: absolute; height: 32px; background: var(--white); border-radius: 9px;
    display: flex; align-items: center;
  }
  .pill::after {
    content: ""; position: absolute; inset: 3px; border: 1px dashed var(--red); border-radius: 7px;
  }
  .pill.tall { height: 38px; }
  .pill.left { left: 133px; width: 225px; padding-left: 90px; }
  .pill.right { left: 434px; width: 258px; padding-left: 84px; }
  .pill-label { font-weight: 800; font-size: 18px; line-height: 0.95; color: var(--red); text-transform: uppercase; }
  .pill-icon {
    position: absolute; top: 50%; left: 13px; width: 54px; height: 54px; margin-top: -27px; border-radius: 50%;
    background: var(--white); border: 2px solid var(--black); z-index: 1;
  }
  .pill-icon span { position: absolute; inset: 7px; border-radius: 50%; background: var(--icon-fill); }
  .solution {
    position: absolute; left: 0; width: 826px; top: 925px; text-align: center;
    font-family: "Roboto Slab", serif; font-weight: 700; font-size: 48px; color: var(--white); line-height: 1;
  }
  .contact-bar {
    position: absolute; left: 98px; top: 988px; width: 630px; height: 35px; background: var(--red);
    text-align: center; font-family: "Roboto Slab", serif; font-weight: 700; font-size: 25px; line-height: 35px; color: var(--white);
  }
  .phone-line {
    position: absolute; left: 0; width: 826px; top: 1036px;
    display: flex; justify-content: center; align-items: center; gap: 16px;
    font-weight: 600; font-size: 31px; letter-spacing: 2px; color: var(--white);
  }
  .phone-line svg { width: 28px; height: 28px; }
  .detail-line {
    position: absolute; left: 0; width: 826px;
    display: flex; justify-content: center; align-items: center; gap: 10px;
    font-weight: 700; font-size: 18px; color: var(--white); white-space: nowrap;
  }
  .detail-line.first { top: 1080px; }
  .detail-line.second { top: 1109px; }
  .detail-line .gap { width: 16px; }
  .mark { width: 16px; height: 16px; background: var(--social); border-radius: 2px; flex: none; }
  .mark.page { background: var(--social-dark); }
</style>
</head>
<body>
<div class="flyer">
  <svg class="dark-field" viewBox="0 0 826 1172" width="826" height="1172" aria-hidden="true">
    <path d="M0,408 H408 V275 C600,268 760,370 826,498 V1172 H0 Z" fill="var(--black)"/>
    <rect x="0" y="0" width="408" height="408" fill="var(--white)"/>
  </svg>

  <div class="photo photo-left" role="img" aria-label="Portrait photo of the founder in profile, platinum hair, dark top"></div>
  <div class="photo photo-right" role="img" aria-label="Close-up photo of half the founder's face with red lips"></div>
  <div class="logo-disc">Velvet<br>Ladder</div>

  <div class="brand">
    <div class="brand-name">#VelvetLadder</div>
    <div class="brand-tagline">Recruitment &amp; People Development</div>
  </div>

  <div class="headline">RECRUITING NOW!</div>
  <div class="subhead">START TODAY &amp; START EARNING!</div>

  <div class="col-heading left">WOULD YOU LIKE AN<br>EXTRA INCOME, FOR...</div>
  <div class="divider"></div>
  <div class="col-heading right">ARE YOU FACING...</div>

  <div class="pill left" style="top:703px"><div class="pill-icon" role="img" aria-label="Palm tree icon"><span></span></div><span class="pill-label">A holiday?</span></div>
  <div class="pill left" style="top:767px"><div class="pill-icon" role="img" aria-label="Car icon"><span></span></div><span class="pill-label">A new car?</span></div>
  <div class="pill left tall" style="top:832px"><div class="pill-icon" role="img" aria-label="Woman with shopping bags icon"><span></span></div><span class="pill-label">Lifestyle<br>changes?</span></div>

  <div class="pill right" style="top:703px"><div class="pill-icon" role="img" aria-label="Seated figure icon"><span></span></div><span class="pill-label">Redundancy?</span></div>
  <div class="pill right" style="top:767px"><div class="pill-icon" role="img" aria-label="Bill in hand icon"><span></span></div><span class="pill-label">Hefty bills?</span></div>
  <div class="pill right tall" style="top:832px"><div class="pill-icon" role="img" aria-label="Baby icon"><span></span></div><span class="pill-label">Birth of a<br>new child?</span></div>

  <div class="solution">IF SO, I HAVE THE SOLUTION.</div>
  <div class="contact-bar">Contact Rosalind Pettigrew today:</div>

  <div class="phone-line">
    <svg viewBox="0 0 28 28" aria-hidden="true">
      <rect width="28" height="28" rx="6" fill="var(--white)"/>
      <path d="M9 6 C7 7 6 9 7 12 C9 17 12 20 16 22 C19 23 21 22 22 20 L19 17 L16.5 18.5 C14 17 11.5 14.5 10 12 L11.5 9.5 Z" fill="var(--red)"/>
    </svg>
    <span>07945 618274</span>
  </div>

  <div class="detail-line first">
    <svg width="20" height="14" viewBox="0 0 20 14" aria-hidden="true">
      <rect x="0.5" y="0.5" width="19" height="13" fill="var(--white)"/>
      <path d="M1 1 L10 8 L19 1 M1 13 L8 6.5 M19 13 L12 6.5" stroke="var(--black)" fill="none" stroke-width="1.3"/>
    </svg>
    <span>Rosalind@velvetladder.co.uk</span>
    <span class="gap"></span>
    <span class="mark"></span>
    <span>@Velvet_Ladder</span>
  </div>
  <div class="detail-line second">
    <span class="mark page"></span>
    <span>www.pagehub.net/rosandvelvetladder</span>
  </div>
</div>
</body>
</html>
```